Kindle Grove Wording For Logo & Business card

I have the logo, I just need the "kindle Grove" wording to go with it, and a business card design. The only thing on the business card is the website info. We provide nature connection experiences, and bolster these efforts through writing and host a platform for community around it.

I also have an idea of what it could look like (sketch), though I'm really not sure how it would come out. I am open to the best design and happy to consider original artwork. You can see what the site is about at KindleGrove.com.

Contact Information for Business Card

The only thing on the business card is the website info and the design. I will put other messaging on the back.

Website lettering (KindleGrove.com) in Montserrat

Logo Text

Kindle Grove (letters optional)

Font styles to use
Other font styles liked:
• montserrat

```html
<!DOCTYPE html>
<html lang="en">
<head>
<meta charset="utf-8">
<title>Kindle Grove – Business Card</title>
<link rel="stylesheet" href="https://fonts.googleapis.com/css2?family=Montserrat:wght@400;500;700;800&display=swap">
<style>
  :root {
    --page-bg: #e6e3df;
    --purple-dark: #34194f;
    --purple-mid: #4b2a6b;
    --purple-light: #5d3c7e;
    --brand-purple: #4a2a68;
    --orange: #e2601a;
    --ink: #4a4a4a;
    --rule: #9a9a9a;
    --white: #ffffff;
  }
  * { box-sizing: border-box; margin: 0; padding: 0; }
  html, body {
    width: 1200px; height: 900px; overflow: hidden;
    background: var(--page-bg);
    font-family: "Montserrat", sans-serif;
  }
  .sheet {
    width: 1200px; height: 900px;
    display: flex; flex-direction: column;
    align-items: center; justify-content: center; gap: 40px;
  }
  .card {
    width: 700px; height: 400px;
    position: relative;
    box-shadow: 0 6px 18px rgba(0,0,0,.18);
  }
  .card--front {
    background: linear-gradient(200deg, var(--purple-dark) 0%, var(--purple-mid) 55%, var(--purple-light) 100%);
    display: flex; align-items: center; justify-content: center;
  }
  .brand { display: flex; align-items: center; gap: 22px; }
  .brand__dot { border-radius: 50%; flex: none; }
  .brand__name {
    font-weight: 800; text-transform: uppercase; letter-spacing: 2px; line-height: 1;
    white-space: nowrap;
  }
  .card--front .brand__dot { width: 120px; height: 120px; background: var(--orange); }
  .card--front .brand__name { color: var(--white); font-size: 46px; }

  .card--back { background: var(--white); }
  .card--back .brand {
    position: absolute; left: 48px; top: 50%; transform: translateY(-50%);
    gap: 14px;
  }
  .card--back .brand__dot { width: 78px; height: 78px; background: var(--brand-purple); }
  .card--back .brand__name { color: var(--brand-purple); font-size: 26px; letter-spacing: 1px; }
  .divider {
    position: absolute; left: 392px; top: 110px; width: 1px; height: 180px;
    background: var(--rule);
  }
  .website {
    position: absolute; left: 424px; top: 50%; transform: translateY(-50%);
    display: flex; align-items: center; gap: 12px;
    font-size: 19px; font-weight: 500; color: var(--ink); white-space: nowrap;
  }
  .website svg { width: 16px; height: 16px; flex: none; }
  .website svg circle, .website svg path { fill: none; stroke: var(--orange); stroke-width: 2; }
</style>
</head>
<body>
<main class="sheet">
  <section class="card card--front" aria-label="Card front">
    <div class="brand">
      <span class="brand__dot"></span>
      <span class="brand__name">Kindle Grove</span>
    </div>
  </section>

  <section class="card card--back" aria-label="Card back">
    <div class="brand">
      <span class="brand__dot"></span>
      <span class="brand__name">Kindle Grove</span>
    </div>
    <div class="divider"></div>
    <p class="website">
      <svg viewBox="0 0 24 24" aria-hidden="true"><circle cx="12" cy="12" r="10"/><path d="M2 12h20M12 2c3 3 3 17 0 20M12 2c-3 3-3 17 0 20"/></svg>
      www.kindlegrove.com
    </p>
  </section>
</main>
</body>
</html>
```